DPM Marketing Postcard

Design a 2 Sided marketing postcard for our Real estate management caompany. Looking for a professional yet fresh look that will be printed on a 6"x9" glossy flier

Contact information is www.dunkeldmanagement-example.com dunkeldmanagement@dunkeldmail-example.com and 312-480-7193

WE are targeting small condo and town home properties to take on their administrative responsibilities of management

```html
<!DOCTYPE html>
<html lang="en">
<head>
<meta charset="utf-8">
<title>DPM Marketing Postcard</title>
<link href="https://fonts.googleapis.com/css2?family=Roboto+Condensed:ital,wght@0,400;0,700;1,700&display=swap" rel="stylesheet">
<style>
:root{
  --page:#1d5585;
  --ink-dark:#0f1c24;
  --band:#2c6a98;
  --band-line:#9fc0da;
  --panel:#21608f;
  --accent:#3a9be0;
  --light:#ffffff;
  --text-dark:#111;
  --url:#3a9be0;
}
*{margin:0;padding:0;box-sizing:border-box}
html,body{width:1200px;height:1200px;overflow:hidden}
body{background:var(--page);font-family:"Roboto Condensed",sans-serif;position:relative}
.card{position:absolute;width:823px;height:556px;overflow:hidden}
.card-front{left:53px;top:22px;background:var(--ink-dark)}
.card-back{left:338px;top:606px;background:#eef1f3}
.card svg.art{position:absolute;left:0;top:0}
.header{position:absolute;left:0;top:28px;width:100%;height:66px;background:rgba(44,106,152,.92);border-top:2px solid var(--band-line);border-bottom:2px solid var(--band-line);display:flex;align-items:center}
.card-back .header{top:26px;height:68px}
.brand{position:absolute;left:24px;display:flex;align-items:center;gap:5px;color:var(--light);font-size:14px;font-weight:400;letter-spacing:.3px}
.brand-mark{width:10px;height:10px;border-radius:50%;background:var(--light)}
.title{position:absolute;left:98px;color:var(--light);font-size:37px;font-weight:400;letter-spacing:.2px;white-space:nowrap}
.benefits{position:absolute;left:456px;top:106px;width:350px;list-style:none;color:var(--light);font-size:17px;line-height:21px}
.benefits li{position:relative;padding-left:25px;margin-bottom:13.5px}
.tick{position:absolute;left:0;top:2px;width:18px;height:16px}
.footer-url{position:absolute;left:30px;color:var(--url);font-size:14px;white-space:nowrap}
.footer-call{position:absolute;right:37px;font-size:19px;font-weight:700;font-style:italic;color:var(--text-dark);white-space:nowrap}
.card-front .footer-url{top:504px}
.card-front .footer-call{top:502px}
.card-back .footer-url{top:504px}
.card-back .footer-call{top:502px}
.tagline{position:absolute;left:65px;top:100px;font-size:17px;line-height:21px;font-weight:700;font-style:italic;color:var(--text-dark)}
.info{position:absolute;left:0;top:0;width:100%;height:100%;color:var(--light)}
.info .h{position:absolute;font-size:16px;font-weight:700;line-height:18px;display:flex;align-items:center;gap:8px;right:0}
.info .h::after{content:"";flex:1;height:1px;background:var(--band-line)}
.info .i{position:absolute;font-size:11px;line-height:13.5px;padding-left:14px;right:20px}
.info .i .tick{width:11px;height:10px;top:1px}
</style>
</head>
<body>

<section class="card card-front">
  <svg class="art" width="823" height="556" viewBox="0 0 823 556">
    <defs>
      <linearGradient id="keyPhoto" x1="0" y1="0" x2="1" y2="1">
        <stop offset="0" stop-color="#1a1a1c"/>
        <stop offset=".45" stop-color="#c9a48c"/>
        <stop offset=".75" stop-color="#2b2624"/>
        <stop offset="1" stop-color="#4a3a30"/>
      </linearGradient>
      <linearGradient id="callBand1" x1="0" y1="0" x2="0" y2="1">
        <stop offset="0" stop-color="#ffffff"/>
        <stop offset=".6" stop-color="#dbe9f5"/>
        <stop offset="1" stop-color="#5a9cd2"/>
      </linearGradient>
    </defs>
    <polygon points="0,0 335,0 410,330 300,493 0,493" fill="url(#keyPhoto)" role="img" aria-label="Photo of a hand dropping a house-shaped key into another open hand above paperwork"/>
    <polygon points="345,0 362,0 443,330 323,493 306,493 425,330" fill="#2c6a98"/>
    <polygon points="0,533 267,533 255,556 0,556" fill="#e9ecef" role="img" aria-label="Photo of paperwork on a desk"/>
    <rect x="0" y="493" width="823" height="40" fill="#0d2a42"/>
    <polygon points="291,493 823,493 823,533 279,533" fill="url(#callBand1)"/>
  </svg>
  <div class="header">
    <div class="brand"><span class="brand-mark"></span>Dunkeld</div>
    <div class="title">DUNKELD PROPERTY MANAGEMENT LLC</div>
  </div>
  <ul class="benefits">
    <li><svg class="tick" viewBox="0 0 18 16"><path d="M1 9l5 5L17 1" fill="none" stroke="#3a9be0" stroke-width="3"/></svg>Cost effective property management solution for 3-10 unit buildings</li>
    <li><svg class="tick" viewBox="0 0 18 16"><path d="M1 9l5 5L17 1" fill="none" stroke="#3a9be0" stroke-width="3"/></svg>Prices starting as low as $100/month</li>
    <li><svg class="tick" viewBox="0 0 18 16"><path d="M1 9l5 5L17 1" fill="none" stroke="#3a9be0" stroke-width="3"/></svg>Utilize our economies of scale to reduce costs across existing services (trash, insurance, maintenance, etc)</li>
    <li><svg class="tick" viewBox="0 0 18 16"><path d="M1 9l5 5L17 1" fill="none" stroke="#3a9be0" stroke-width="3"/></svg>Eliminate the unfair burden placed on a few owners to do all the work while others free-ride</li>
    <li><svg class="tick" viewBox="0 0 18 16"><path d="M1 9l5 5L17 1" fill="none" stroke="#3a9be0" stroke-width="3"/></svg>Improve communication amongst all owners and board members</li>
    <li><svg class="tick" viewBox="0 0 18 16"><path d="M1 9l5 5L17 1" fill="none" stroke="#3a9be0" stroke-width="3"/></svg>The association’s board of directors maintain all decision-making power</li>
    <li><svg class="tick" viewBox="0 0 18 16"><path d="M1 9l5 5L17 1" fill="none" stroke="#3a9be0" stroke-width="3"/></svg>Utilize our vetted service providers for prompt job completion and fair pricing</li>
  </ul>
  <div class="footer-url">www.dunkeldmanagement-example.com</div>
  <div class="footer-call">CALL US NOW FOR MORE INFO : 312-480-7193</div>
</section>

<section class="card card-back">
  <svg class="art" width="824" height="556" viewBox="0 0 824 556">
    <defs>
      <linearGradient id="meetingPhoto" x1="0" y1="0" x2="1" y2="1">
        <stop offset="0" stop-color="#f7f8f8"/>
        <stop offset=".5" stop-color="#d9d5cf"/>
        <stop offset=".8" stop-color="#6c7380"/>
        <stop offset="1" stop-color="#2a3240"/>
      </linearGradient>
      <linearGradient id="topStrip" x1="0" y1="0" x2="1" y2="0">
        <stop offset="0" stop-color="#f4f6f7"/>
        <stop offset=".55" stop-color="#e3e8ec"/>
        <stop offset=".56" stop-color="#2c6a98"/>
        <stop offset="1" stop-color="#2c6a98"/>
      </linearGradient>
      <linearGradient id="callBand2" x1="0" y1="0" x2="0" y2="1">
        <stop offset="0" stop-color="#ffffff"/>
        <stop offset=".6" stop-color="#dbe9f5"/>
        <stop offset="1" stop-color="#5a9cd2"/>
      </linearGradient>
    </defs>
    <rect x="0" y="0" width="824" height="28" fill="url(#topStrip)"/>
    <rect x="0" y="94" width="824" height="398" fill="url(#meetingPhoto)" role="img" aria-label="Photo of a young couple reviewing documents with a property manager in a bright living room"/>
    <polygon points="0,94 330,94 330,220 0,220" fill="#f5f6f6" opacity=".85"/>
    <polygon points="376,94 824,94 824,492 320,492 436,326" fill="var(--panel)"/>
    <polygon points="362,94 376,94 436,326 320,492 306,492 422,326" fill="#16324a"/>
    <polygon points="0,534 280,534 268,556 0,556" fill="#c8d9a4" role="img" aria-label="Photo of a green houseplant"/>
    <rect x="0" y="492" width="824" height="42" fill="#0d2a42"/>
    <polygon points="310,492 824,492 824,534 286,534" fill="url(#callBand2)"/>
  </svg>
  <div class="header">
    <div class="brand"><span class="brand-mark"></span>Dunkeld</div>
    <div class="title">DUNKELD PROPERTY MANAGEMENT LLC</div>
  </div>
  <p class="tagline">Improve compliance, reporting,<br>and communication amongst<br>all owners and board members</p>
  <div class="info">
    <div class="h" style="left:411px;top:111px">Who we are</div>
    <div class="i" style="left:416px;top:135px"><svg class="tick" viewBox="0 0 18 16"><path d="M1 9l5 5L17 1" fill="none" stroke="#fff" stroke-width="3"/></svg>A professional services organization with a focus on small (3-10 unit)<br>&nbsp;&nbsp;residential buildings</div>
    <div class="i" style="left:423px;top:162px"><svg class="tick" viewBox="0 0 18 16"><path d="M1 9l5 5L17 1" fill="none" stroke="#fff" stroke-width="3"/></svg>Over 30 years of combined experience in real estate and property management</div>
    <div class="i" style="left:427px;top:175px"><svg class="tick" viewBox="0 0 18 16"><path d="M1 9l5 5L17 1" fill="none" stroke="#fff" stroke-width="3"/></svg>Professional, courteous, timely service that is technologically driven</div>
    <div class="h" style="left:434px;top:198px">Why use DPM?</div>
    <div class="i" style="left:438px;top:221px"><svg class="tick" viewBox="0 0 18 16"><path d="M1 9l5 5L17 1" fill="none" stroke="#fff" stroke-width="3"/></svg>Owners are rarely suited to manage associations and the burden often<br>&nbsp;&nbsp;falls unfairly on one or two individuals to do all the work</div>
    <div class="i" style="left:450px;top:248px"><svg class="tick" viewBox="0 0 18 16"><path d="M1 9l5 5L17 1" fill="none" stroke="#fff" stroke-width="3"/></svg>Low monthly fees tailored to your needs</div>
    <div class="i" style="left:454px;top:262px"><svg class="tick" viewBox="0 0 18 16"><path d="M1 9l5 5L17 1" fill="none" stroke="#fff" stroke-width="3"/></svg>The association’s board of directors maintains control of all decision making</div>
    <div class="h" style="left:456px;top:283px">What we do</div>
    <div class="i" style="left:462px;top:306px"><svg class="tick" viewBox="0 0 18 16"><path d="M1 9l5 5L17 1" fill="none" stroke="#fff" stroke-width="3"/></svg>Remove the administrative burden of managing small residential buildings</div>
    <div class="i" style="left:463px;top:324px"><svg class="tick" viewBox="0 0 18 16"><path d="M1 9l5 5L17 1" fill="none" stroke="#fff" stroke-width="3"/></svg>Utilize economies of scale to reduce expenses for all owners across a wide<br>variety of service providers</div>
    <div class="i" style="left:446px;top:355px"><svg class="tick" viewBox="0 0 18 16"><path d="M1 9l5 5L17 1" fill="none" stroke="#fff" stroke-width="3"/></svg>Collect all assessments and pay all bills</div>
    <div class="i" style="left:434px;top:374px"><svg class="tick" viewBox="0 0 18 16"><path d="M1 9l5 5L17 1" fill="none" stroke="#fff" stroke-width="3"/></svg>Provide monthly accounting reconciliation and reporting</div>
    <div class="i" style="left:423px;top:391px"><svg class="tick" viewBox="0 0 18 16"><path d="M1 9l5 5L17 1" fill="none" stroke="#fff" stroke-width="3"/></svg>Provide access to DPM’s client portal with a central repository of all association<br>materials (bylaws, financials, meeting minutes, communications, etc)</div>
    <div class="i" style="left:411px;top:419px"><svg class="tick" viewBox="0 0 18 16"><path d="M1 9l5 5L17 1" fill="none" stroke="#fff" stroke-width="3"/></svg>Issue 1099s to all contractors as required by law</div>
    <div class="i" style="left:398px;top:438px"><svg class="tick" viewBox="0 0 18 16"><path d="M1 9l5 5L17 1" fill="none" stroke="#fff" stroke-width="3"/></svg>Prepare year-end financial statements</div>
    <div class="i" style="left:387px;top:457px"><svg class="tick" viewBox="0 0 18 16"><path d="M1 9l5 5L17 1" fill="none" stroke="#fff" stroke-width="3"/></svg>Lender and legal HOA documents for mortgage companies and sale</div>
  </div>
  <div class="footer-url">www.dunkeldmanagement-example.com</div>
  <div class="footer-call">CALL US NOW FOR MORE INFO :&nbsp; 312-480-7193</div>
</section>

</body>
</html>
```